International Hand & Body company needing a Hand cream tube design for the Retail market

I am wanting a modern design for a new range of 6 hand creams I will be launching in August. They need to compliment our range of wrapped soaps which you can see on www.plomvane.com.au so am wanting clean designs. I am wanting a solid colour with a hand drawn organic feel line drawing in black elegantly placed wrapping around the label. I am wanting to focus on the colour and positioning of words and fonts. I like modern clean contemporary fonts. The final design needs to appeal to the broader female market.This may lead to range expansion if designs are well received.
Updates

These designs are not hitting the brief. They are too generic and look like a supermarket brand. Our brand is more boutique and this design needs to be modern and simple. I would like more solid colours and more modern designs. Without patterns.

Target Market(s)

Female aged 20 - 70

Requirements
Must have
• a modern contemporary design that will appeal to the masses.
• Please read attached brief.
Should not have
• a black botanical illustration, in a loose and organic design to match the fragrance.

```html
<!DOCTYPE html>
<html lang="en">
<head>
<meta charset="utf-8">
<title>Plomvane Hand Cream Range</title>
<link rel="stylesheet" href="https://fonts.googleapis.com/css2?family=Open+Sans:wght@400;700&display=swap">
<style>
  :root {
    --page-bg: #ffffff;
    --tube-white: #f4f4f4;
    --crimp-grey: #dcdcdc;
    --cap-black: #141414;
    --ink-dark: #2b2d33;
    --ink-white: #ffffff;
    --citrus-label: #cddf7a;
    --citrus-body: #d7e69c;
    --fig-label: #e5667a;
    --fig-body: #ef8797;
    --yuzu-label: #9ad5c9;
    --yuzu-body: #c6e4ef;
  }
  html, body {
    margin: 0;
    padding: 0;
    width: 1200px;
    height: 790px;
    overflow: hidden;
    background: var(--page-bg);
  }
  .range-display {
    display: block;
    width: 1200px;
    height: 790px;
    font-family: "Open Sans", Arial, sans-serif;
  }
  .tube-body { fill: var(--tube-white); }
  .tube-crimp { fill: var(--crimp-grey); }
  .tube-cap { fill: var(--cap-black); }
  .brand-name { fill: var(--ink-dark); font-size: 36px; font-weight: 400; letter-spacing: 5px; }
  .scent-name { fill: var(--ink-white); font-size: 20px; font-weight: 700; }
  .product-type { fill: var(--ink-dark); font-size: 18px; font-weight: 400; }
  .product-claim { fill: var(--ink-white); font-size: 19.5px; font-weight: 400; }
  .origin-note { fill: var(--ink-white); font-size: 14px; font-weight: 400; }
  .origin-rule { stroke: var(--ink-white); stroke-width: 2; }
  .net-volume { fill: var(--ink-dark); font-size: 19px; font-weight: 400; }
  .citrus .label-panel { fill: var(--citrus-label); }
  .citrus .body-colour { fill: var(--citrus-body); }
  .fig .label-panel { fill: var(--fig-label); }
  .fig .body-colour { fill: var(--fig-body); }
  .yuzu .label-panel { fill: var(--yuzu-label); }
  .yuzu .body-colour { fill: var(--yuzu-body); }
</style>
</head>
<body>
<svg class="range-display" viewBox="0 0 1360 895" preserveAspectRatio="xMidYMid meet" xmlns="http://www.w3.org/2000/svg">
  <defs>
    <g id="tube-shell">
      <rect class="tube-crimp" x="137" y="110" width="276" height="20"/>
      <path class="tube-body" d="M137 130 H413 L407 700 H195 Z"/>
    </g>
    <path id="tube-lower" d="M191 560 L410 470 L407 700 H195 Z"/>
    <path id="tube-cap" d="M197 697 H405 V800 Q405 812 393 812 H209 Q197 812 197 800 Z"/>
    <g id="tube-copy">
      <text class="brand-name" x="284" y="202" text-anchor="middle">plomvane</text>
      <text class="product-type" x="357" y="377" text-anchor="end">Hand Cream</text>
      <text class="product-claim" text-anchor="end">
        <tspan x="357" y="424">A nourishing</tspan>
        <tspan x="357" y="449">non-greasy</tspan>
        <tspan x="357" y="474">hand cream to</tspan>
        <tspan x="357" y="499">keep skin</tspan>
        <tspan x="357" y="524">soft &amp; hydrated</tspan>
      </text>
      <line class="origin-rule" x1="216" y1="545" x2="357" y2="545"/>
      <text class="origin-note" x="357" y="568" text-anchor="end">Made in Australia</text>
      <text class="net-volume" x="301" y="670" text-anchor="middle">35ml ℮ 1.18 fl.oz.</text>
    </g>
  </defs>

  <g class="tube citrus">
    <use href="#tube-shell"/>
    <use class="body-colour" href="#tube-lower"/>
    <rect class="label-panel" x="193" y="282" width="184" height="298"/>
    <use href="#tube-cap" class="tube-cap"/>
    <use href="#tube-copy"/>
    <text class="scent-name" text-anchor="end">
      <tspan x="360" y="320">CITRUS &amp;</tspan>
      <tspan x="360" y="346">SEAGRASS</tspan>
    </text>
  </g>

  <g class="tube fig" transform="translate(378 0)">
    <use href="#tube-shell"/>
    <use class="body-colour" href="#tube-lower"/>
    <rect class="label-panel" x="157" y="284" width="225" height="296"/>
    <use href="#tube-cap" class="tube-cap"/>
    <use href="#tube-copy"/>
    <text class="scent-name" text-anchor="end">
      <tspan x="364" y="320">FIG &amp;</tspan>
      <tspan x="364" y="346">SANDALWOOD</tspan>
    </text>
  </g>

  <g class="tube yuzu" transform="translate(756 0)">
    <use href="#tube-shell"/>
    <use class="body-colour" href="#tube-lower"/>
    <rect class="label-panel" x="158" y="284" width="214" height="296"/>
    <use href="#tube-cap" class="tube-cap"/>
    <use href="#tube-copy"/>
    <text class="scent-name" x="363" y="332" text-anchor="end">YUZU &amp; SAGE</text>
  </g>
</svg>
</body>
</html>
```